Greeting card special spring

Context: I missed the end of the year wishes and would like to send my clients a spring card with a smell of lily of the valley that is 11cm by 11 cm and has a vintage look. This A5 card will be sent in a green envelope with the small ordering bag. I will like the target notes the intent and the associated gaiety My business is HR / Leadership and my clients are responsible for business or HR. Esprit: To keep a spirit of sobriete and elegance but with gaiety. Color: our graphic charter is generally black and gray but for this theme we can shift in color more "spring" taking again the green of the sachet of lily of the valley which is joined in particular to illustrate the notions energy, renewal. (Attached the picture). No photo. Just text and logo. Play on composition and fonts; I have put the elements of typos and fonts as well as taglines and examples of compositions already made (business card, correspondence card, letter paper). One of the elements of the graphic chart is an "e" that is done in brush. If you wish you can play with this graphic elements. Also look at the picture of the perfume pouch that I would attach Format: a card a format A5 or format postcard (format printoubly). The text is composed of 2 elements: Major Text The Velnorath team wishes you a spring full of renewal, fulfillment and creative energy to disseminate absolutely around you. Text minor: Lily of the Valley: Omen of happiness that brings luck to breathe with serenity! Include Logo See contact details Odile Mercanson-Tabry - odile.mercanson@velnorath-mail.net

Target Market(s)

Senior managers, human resource managers

Industry/Entity Type

Management Consulting

Other font styles liked:
• merci d'essayer de rester aligner ou en logique avec les polices/charte graphique envoyees

Requirements
Must have
• Format: one card in A5 format or postcard format (printoubly format). The text is composed of 2 elements: Major Text The Velnorath team wishes you a spring full of renewal, fulfillment and creative energy to disseminate absolutely around you. Text minor: Lily of the Valley: Omen of happiness that brings luck to breathe with serenity! Include Logo See contact details Odile Mercanson-Tabry - odile.mercanson@velnorath-mail.net
Nice to have
• Graphical guideline :. Esprit: To keep a spirit of sobriete and elegance but with gaiety. Color: our graphic charter is generally black and gray but for this theme we can shift in color more "spring" taking again the green of the sachet of lily of the valley which is joined in particular to illustrate the notions energy, renewal. (Attached the picture). Grapic elements; I have put the elements of typos and fonts as well as the examples of compositions already made (business card, correspondence card, letter paper). One of the elements of the logo is an "e" that is made in brush on which you can play. Also look at the image of the perfume pouch that I would join
Should not have
• No photo. Just text and logo. Play on composition and fonts

```html
<!DOCTYPE html>
<html lang="fr">
<head>
<meta charset="utf-8">
<title>Velnorath – Carte de printemps</title>
<link href="https://fonts.googleapis.com/css2?family=Parisienne&family=Jost:wght@400&display=swap" rel="stylesheet">
<style>
  :root {
    --paper: #ffffff;
    --sage-text: #6f8a64;
    --spring-green: #a3b54e;
    --frame-line: #7d8c72;
    --on-green: #ffffff;
  }
  html, body {
    margin: 0;
    padding: 0;
    overflow: hidden;
    background: var(--paper);
  }
  .card {
    position: relative;
    width: 1200px;
    height: 846px;
    background: var(--paper);
    overflow: hidden;
    font-family: "Jost", "Futura", sans-serif;
  }
  .contact-band {
    position: absolute;
    left: 0;
    top: 553px;
    width: 1200px;
    height: 293px;
    background: var(--spring-green);
  }
  .card-frame {
    position: absolute;
    left: 31px;
    top: 32px;
    width: 1126px;
    height: 779px;
    border: 2px solid var(--frame-line);
  }
  .greeting {
    position: absolute;
    left: 128px;
    top: 104px;
    margin: 0;
    font-family: "Parisienne", cursive;
    font-weight: 400;
    font-size: 69px;
    line-height: 76px;
    color: var(--sage-text);
    white-space: nowrap;
  }
  .greeting span { display: block; }
  .motto {
    position: absolute;
    left: 132px;
    top: 483px;
    margin: 0;
    font-size: 21px;
    color: var(--sage-text);
  }
  .brand {
    position: absolute;
    left: 230px;
    top: 636px;
    width: 316px;
    text-align: center;
    color: var(--on-green);
  }
  .brand-mark {
    display: block;
    width: 14px;
    height: 14px;
    margin: 0 auto 50px;
    border-radius: 50%;
    background: var(--on-green);
  }
  .brand-name {
    margin: 0;
    font-size: 28px;
    letter-spacing: 0.22em;
    padding-left: 0.22em;
    line-height: 1;
  }
  .brand-tagline {
    margin: 18px 0 0;
    font-size: 13px;
    letter-spacing: 0.08em;
  }
  .divider {
    position: absolute;
    left: 564px;
    top: 603px;
    width: 2px;
    height: 176px;
    background: rgba(255, 255, 255, 0.7);
  }
  .contact {
    position: absolute;
    left: 606px;
    top: 613px;
    color: var(--on-green);
    font-style: normal;
  }
  .contact-name {
    margin: 0 0 12px;
    font-size: 25px;
    font-weight: 400;
  }
  .contact-phones {
    margin: 0 0 12px;
    font-size: 23px;
    line-height: 27px;
  }
  .contact-email {
    margin: 0;
    font-size: 23px;
  }
</style>
</head>
<body>
  <main class="card">
    <div class="contact-band"></div>
    <div class="card-frame"></div>

    <h1 class="greeting">
      <span>L’équipe de Velnorath vous souhaite</span>
      <span>un printemps plein d’énergie créatrice</span>
      <span>à diffuser absolument autour de vous.</span>
    </h1>

    <p class="motto">Muguet: présage de bonheur à respirer avec sérénité</p>

    <div class="brand">
      <span class="brand-mark"></span>
      <p class="brand-name">VELNORATH</p>
      <p class="brand-tagline">Conseil • Accompagnement</p>
    </div>

    <div class="divider"></div>

    <address class="contact">
      <p class="contact-name">Odile MERCANSON-TABRY</p>
      <p class="contact-phones">+33 (0)6 41 27 93 08 (France)<br>+1 555 014 27 63 (US)</p>
      <p class="contact-email">odile.mercanson@velnorath-mail.net</p>
    </address>
  </main>
</body>
</html>
```